Business Card Design

Rubber roller servicing company. Specializing in rubber to metal bonding. Serving various industries including, pharmaceutical, textile, plastic extrusion, polythene bag converting, laminating and the food industries.

Industry/Entity Type

Plastic

Contact Information for Business Card

Carwick Roller & Rubber Co Ltd, Trevor Ambleside, Managing Director, Unit at Fernholt, Ridley Lane, Oxenby, Marrowby, Westmarsh, HX4 9TJ, Tel 01632 960481, Fax 01632 960527, email info@carwickroller.example.co.uk,

```html
<!DOCTYPE html>
<html lang="en">
<head>
<meta charset="utf-8">
<title>Carwick Roller business card</title>
<link rel="stylesheet" href="https://fonts.googleapis.com/css2?family=Arimo:wght@400;700&display=swap">
<style>
  :root {
    --ink: #0b0b0b;
    --paper: #ffffff;
    --accent: #e0781c;
    --backdrop: #e6e4e1;
    --soft-text: #f2f2f2;
  }
  * { margin: 0; padding: 0; box-sizing: border-box; }
  html, body {
    width: 1200px; height: 564px; overflow: hidden;
    background: var(--backdrop);
    font-family: "Arimo", Arial, sans-serif;
  }
  .card {
    position: absolute; left: 250px; top: 82px;
    width: 700px; height: 400px;
    border-radius: 24px; overflow: hidden;
    background: var(--paper);
    box-shadow: 0 6px 18px rgba(0,0,0,0.18);
  }
  .card-shapes { position: absolute; inset: 0; }
  .brand {
    position: absolute; top: 48px; left: 0; width: 100%;
    text-align: center;
    font-size: 46px; font-weight: 700; letter-spacing: 6px;
    color: var(--ink);
  }
  .company {
    position: absolute; left: 40px; top: 166px;
    font-size: 18px; font-weight: 700; color: var(--accent);
  }
  .contact { position: absolute; left: 40px; color: var(--soft-text); font-size: 14px; }
  .contact-row { display: flex; align-items: flex-start; gap: 14px; }
  .contact-row svg { flex: none; margin-top: 1px; }
  .address { top: 194px; line-height: 17px; }
  .phone { top: 262px; }
  .fax { top: 296px; }
  .email { top: 330px; }
  .person {
    position: absolute; right: 48px; top: 184px; text-align: right;
  }
  .person-name { font-size: 20px; font-weight: 700; color: var(--accent); }
  .person-role { font-size: 13px; font-weight: 700; color: var(--paper); margin-top: 4px; }
  .tagline {
    position: absolute; left: 160px; width: 480px; top: 367px;
    text-align: center; font-size: 15px; font-weight: 700; color: var(--accent);
  }
</style>
</head>
<body>
  <div class="card">
    <svg class="card-shapes" width="700" height="400" viewBox="0 0 700 400" aria-hidden="true">
      <polygon points="0,158 700,132 700,400 0,400" fill="var(--ink)"/>
      <path d="M160,400 L160,385 Q160,355 190,355 L610,355 Q640,355 640,385 L640,400 Z" fill="var(--paper)"/>
    </svg>

    <div class="brand">CARWICKROLLER</div>

    <div class="company">Carwick Roller &amp; Rubber Co Ltd</div>

    <div class="contact address contact-row">
      <svg width="12" height="16" viewBox="0 0 12 16"><path d="M6 0C2.7 0 0 2.6 0 5.9 0 10 6 16 6 16s6-6 6-10.1C12 2.6 9.3 0 6 0zm0 8.3A2.4 2.4 0 1 1 6 3.5a2.4 2.4 0 0 1 0 4.8z" fill="var(--accent)"/></svg>
      <div>Fernholt, Ridley Lane,<br>Oxenby, Marrowby,<br>Westmarsh, HX4 9TJ</div>
    </div>

    <div class="contact phone contact-row">
      <svg width="12" height="16" viewBox="0 0 12 16"><rect x="1" y="0.8" width="10" height="14.4" rx="2" fill="none" stroke="var(--accent)" stroke-width="1.6"/><circle cx="6" cy="12.4" r="1" fill="var(--accent)"/></svg>
      <div>01632 960481</div>
    </div>

    <div class="contact fax contact-row">
      <svg width="12" height="14" viewBox="0 0 14 14"><rect x="3" y="0" width="8" height="5" fill="var(--accent)"/><rect x="0" y="5" width="14" height="9" rx="1.5" fill="var(--accent)"/><rect x="3" y="8" width="8" height="3" fill="var(--ink)"/></svg>
      <div>01632 960527</div>
    </div>

    <div class="contact email contact-row">
      <svg width="12" height="11" viewBox="0 0 14 11"><rect x="0" y="0" width="14" height="11" rx="1" fill="var(--accent)"/><path d="M0.5 0.8 L7 6 L13.5 0.8" fill="none" stroke="var(--ink)" stroke-width="1.3"/></svg>
      <div>info@carwickroller.example.co.uk,</div>
    </div>

    <div class="person">
      <div class="person-name">Trevor Ambleside</div>
      <div class="person-role">Managing Director</div>
    </div>

    <div class="tagline">Specializing in rubber to metal bonding</div>
  </div>
</body>
</html>
```